Australian Grown Coffee needs a premium, OUTSTANDING!! Coffee bag design

Morrell coffee is a family owned and run company with coffee being in our blood, currently being run by 3rd gen coffee farmers with roots tying back to coffee growing in Tanzania. We grow, process and roast a very high quality Arabica Coffee (It has won the Gold/ The best milk based coffee in Australia at the silver kettle prizes in the past). We package our coffee beans and ground coffee into 1kg and 250gram bags, which are a bit dated now. We would love to get some amazing designs to bring our product into the future. Our target audience would be 25yrs- 60yr old with a large proportion coming to our plantation to do a tour enjoy a cup, take home a momento and then turn into an online customer.
Content
We would like to achieve a modern standout packaging design that reflects our premium quality Australian coffee. We have a medium roast and an espresso roast lines that we grow roast and sell.
We are happy to see designs that are creative and unique, not just another coffee bag on the shelf, but a standout premium product, that reflects that the coffee is actually grown in Australia, not just roasted here.
Our current colours are red and gold, and we are looking to package our coffee in box bottom bags with rippa zippas with both the 1kg and 250 gram lines, but are open to any other fantastic packaging concepts too.
The bag need to communicate the high quality of the bean within.
Some brainstormed keywords are: Australian, Fresh, Single Origin, Premium, Reserve, Cafe, Barista, Very High Quality, Grown, Plantation.

Target Market(s)

The target market is 25yrs+

Industry/Entity Type

It Company

Font styles to use
Sans Serif
Script

Colors
ec1f27
ffffff
ffc214
0792cd
9bcb3c

Requirements
Must have
• A unique design that stands out from all the rest, ie I'll buy this one! It is more expensive but the package looks so premium i don't mind paying extra for it.
• -Name of roast:(Espresso Roast, Beans), (Espresso Roast, Fine Grind), (Medium Roast beans), ( Medium roast, Plunger/Drip Grind).
• - An area on the back of the package for a barcode Ean13.
Nice to have
• Class added, either in a fancy emblem (think Australian nation emblem except better :)
• Something really attractive in the side gussets
• Clear and concise, uncluttered.
Should not have
• Just a picture of a kangaroo/ koala...

```html
<!DOCTYPE html>
<html lang="en">
<head>
<meta charset="utf-8">
<title>Morrell Coffee – Espresso Roast Bag</title>
<link rel="stylesheet" href="https://fonts.googleapis.com/css2?family=Open+Sans:ital,wght@0,400;0,600;0,700;1,700&family=Oswald:wght@300;400&display=swap">
<style>
  :root {
    --bag-red: #e4211f;
    --bag-red-deep: #b8141a;
    --gold: #ffc214;
    --gold-light: #fff3b8;
    --ink: #0d0d0d;
    --white: #ffffff;
    --leaf: #3f7a2a;
    --leaf-light: #9bcb3c;
    --stage: #f2f2f2;
  }
  * { margin: 0; padding: 0; box-sizing: border-box; }
  html, body { width: 1200px; height: 979px; overflow: hidden; }
  body {
    background: var(--stage);
    font-family: "Open Sans", Arial, sans-serif;
    position: relative;
  }

  .bag { position: absolute; left: 430px; top: 130px; width: 392px; height: 730px; display: flex; }

  /* Front panel */
  .front { position: relative; width: 332px; height: 100%; background: var(--bag-red); overflow: hidden; }
  .seal-band {
    height: 128px;
    background: linear-gradient(90deg, var(--gold) 0%, var(--gold-light) 22%, var(--white) 40%, var(--white) 62%, var(--gold-light) 80%, var(--gold) 100%);
    position: relative;
    border-bottom: 3px solid var(--gold);
  }
  .seal-band svg { position: absolute; left: 104px; top: 8px; }
  .brand { position: absolute; left: 0; right: 0; top: 208px; text-align: center; color: var(--white); }
  .brand-name { font-size: 30px; font-weight: 400; letter-spacing: 1px; line-height: 1; }
  .brand-line { font-size: 14px; font-weight: 700; margin-top: 8px; }

  .map {
    position: absolute; left: 50px; top: 285px; width: 250px; height: 225px;
    border-radius: 6px;
    background: radial-gradient(ellipse at 50% 45%, var(--ink) 0%, var(--ink) 55%, rgba(13,13,13,0.55) 80%, rgba(13,13,13,0) 100%);
  }
  .roast-name {
    position: absolute; left: 0; right: 0; top: 358px; text-align: center;
    font-family: "Oswald", "Arial Narrow", sans-serif; font-weight: 300;
    font-size: 44px; letter-spacing: 0.5px; line-height: 1; color: transparent;
    -webkit-text-stroke: 1.4px var(--white);
  }
  .plantation {
    position: absolute; left: 0; right: 0; top: 500px; height: 72px;
    background: linear-gradient(180deg, rgba(63,122,42,0) 0%, var(--leaf) 35%, var(--leaf-light) 60%, var(--leaf) 80%, var(--ink) 100%);
  }
  .tagline-band {
    position: absolute; left: 0; right: 0; top: 572px; height: 50px;
    background: var(--ink); border-bottom: 3px solid var(--gold);
    color: var(--white); font-size: 12px; padding: 22px 0 0 63px;
  }
  .grind { position: absolute; left: 0; right: 0; top: 641px; text-align: center; font-size: 9px; color: #3a0a0a; }
  .weight { position: absolute; left: 0; right: 0; top: 662px; text-align: center; font-size: 20px; color: var(--ink); }
  .valve { position: absolute; top: 656px; width: 22px; height: 22px; border-radius: 50%; background: #f0b6b2; }
  .valve.left { left: 54px; }
  .valve.right { right: 74px; }

  /* Side gusset */
  .gusset {
    width: 60px; height: 100%; background: var(--ink); color: var(--white);
    padding: 318px 4px 0; font-size: 5px; line-height: 1.5;
    display: flex; flex-direction: column; align-items: center; gap: 8px;
  }
  .gusset p { text-align: center; }
  .award { width: 20px; height: 20px; border-radius: 50%; background: var(--gold); border: 2px solid var(--ink); box-shadow: 0 0 0 1px var(--gold); }
  .gusset-teeth { margin-top: auto; margin-bottom: 10px; }

  .note {
    position: absolute; left: 648px; top: 902px;
    font-style: italic; font-weight: 700; font-size: 22px; color: var(--ink);
  }
  .note-arrow { position: absolute; left: 858px; top: 772px; }
</style>
</head>
<body>
  <div class="bag">
    <section class="front">
      <div class="seal-band">
        <svg width="104" height="16" viewBox="0 0 104 16" aria-hidden="true">
          <g fill="#e4211f">
            <polygon points="0,0 16,0 8,14"/><polygon points="18,0 34,0 26,14"/>
            <polygon points="36,0 52,0 44,14"/><polygon points="54,0 70,0 62,14"/>
            <polygon points="72,0 88,0 80,14"/><polygon points="88,0 104,0 96,14"/>
          </g>
        </svg>
      </div>
      <div class="brand">
        <div class="brand-name">MORRELL</div>
        <div class="brand-line">AUSTRALIAN COFFEE</div>
      </div>
      <div class="map" role="img" aria-label="Black silhouette map of Australia"></div>
      <h1 class="roast-name">ESPRESSO ROAST</h1>
      <div class="plantation" role="img" aria-label="Photograph of green coffee plantation foliage"></div>
      <div class="tagline-band">Our bold, rich 100% Arabica roast</div>
      <div class="grind">Whole Bean | Ground</div>
      <span class="valve left"></span>
      <div class="weight">250g</div>
      <span class="valve right"></span>
    </section>

    <aside class="gusset">
      <p>Brew the perfect cup with our hand roasted beans</p>
      <span class="award"></span>
      <p>Grown, picked and roasted on our family plantation for a rich, smooth cup.</p>
      <span class="award"></span>
      <p>Espresso Machine: use a fine grind and a firm tamp for a full crema.</p>
      <span class="award"></span>
      <p>Plunger: use a coarse grind and steep for four minutes before pressing.</p>
      <svg class="gusset-teeth" width="40" height="10" viewBox="0 0 40 10" aria-hidden="true">
        <g fill="#e4211f">
          <polygon points="0,10 6,0 12,10"/><polygon points="14,10 20,0 26,10"/><polygon points="28,10 34,0 40,10"/>
        </g>
      </svg>
    </aside>
  </div>

  <svg class="note-arrow" width="110" height="100" viewBox="0 0 110 100" aria-hidden="true">
    <path d="M104 94 C80 70 40 40 10 10" fill="none" stroke="#0d0d0d" stroke-width="2"/>
    <path d="M10 10 L12 28 M10 10 L28 12" fill="none" stroke="#0d0d0d" stroke-width="2"/>
  </svg>
  <p class="note">Alternative: black sides with awards</p>
</body>
</html>
```